FLYERENTWURF  für Make up Ausbildung
FLYERENTWURF für Make up Ausbildung
Zielgruppe
friseure die sich weiterbilden wollen
Aufgabenstellung
zu entwerfen ist ein doppelseitiger flyer in A4, zweimal gefalten.
außenseite:
erste spalte/deckblatt:
das logo (im anhang)
schriftzug: mira make up academy
eventuell bild kussmund, wenn rechte vorhanden.
zweite spalte/hinterseite:
zahlungsbedingungen (text wird noch beigefügt)
dritte spalte:
personenbild (anhang)
personenbeschreibung (text wird noch beigefügt)
innenseite:
text aus anhang

```html
<!DOCTYPE html>
<html lang="de">
<head>
<meta charset="utf-8">
<title>mira make up academy – Flyer</title>
<link href="https://fonts.googleapis.com/css2?family=Open+Sans:wght@400;600;700&display=swap" rel="stylesheet">
<style>
:root{
  --stage:#8a8a8a;
  --navy:#0d1326;
  --blue:#2f4a8c;
  --blue-light:#8fc2ea;
  --red:#c8352b;
  --lavender:#e7e9f6;
  --head-blue:#6ea6de;
  --pink:#e0609c;
  --ink:#3a3f55;
  --white:#ffffff;
}
*{margin:0;padding:0;box-sizing:border-box}
html,body{width:1200px;height:900px;overflow:hidden}
body{background:var(--stage);font-family:"Open Sans",sans-serif;position:relative}
.sheet{position:absolute;width:640px;height:438px;overflow:hidden;box-shadow:0 0 14px rgba(255,255,255,.5)}
.sheet--outside{left:520px;top:8px;background:var(--blue)}
.sheet--inside{left:40px;top:455px;background:var(--lavender)}
.top-strip{position:absolute;left:0;top:0;width:100%;height:22px;background:var(--navy)}
.bottom-wave{position:absolute;left:0;bottom:0;width:100%;height:40px}
.photo{position:absolute}
.col{position:absolute;color:var(--white);font-size:6px;line-height:1.35}
.title-red{color:var(--red);font-size:10px;font-weight:700;margin-bottom:6px}

/* outside */
.person-photo{left:24px;top:56px;width:112px;height:152px;border:2px solid var(--white);background:linear-gradient(160deg,#4a3a36,#b89482 60%,#2a2a2a)}
.col--person{left:20px;top:226px;width:190px}
.col--payment{left:226px;top:46px;width:196px}
.detail-photo{left:226px;width:104px;height:72px;border:2px solid var(--white);background:linear-gradient(120deg,#f1efef,#c9c2c4)}
.detail-photo--eye{top:198px}
.detail-photo--lips{top:286px;background:linear-gradient(120deg,#ece6e6,#b36a6a)}
.cover{position:absolute;right:0;top:22px;width:206px;height:388px;background:linear-gradient(180deg,#f2f2f4,#cfcfd6 60%,#5a5660)}
.cover-title{position:absolute;right:16px;top:100px;width:120px;text-align:right;color:var(--red);font-size:17px;font-weight:700;line-height:1.05}
.brand{position:absolute;right:16px;top:340px;text-align:right;color:var(--red)}
.brand-name{font-size:32px;font-weight:700;line-height:1}
.brand-sub{font-size:7px;font-weight:400;line-height:1.3}

/* inside */
.inside-photo{position:absolute;left:0;top:22px;width:250px;height:380px;background:linear-gradient(90deg,#b9bdd4,#dcdff0 80%,var(--lavender))}
.course{position:absolute;top:28px;width:196px;color:var(--ink);font-size:6px;line-height:1.35}
.course--one{left:12px;top:52px}
.course--two{left:222px}
.course--three{left:428px}
.course h2{color:var(--head-blue);font-size:11px;font-weight:700;line-height:1.3;margin-bottom:5px}
.course h3{color:var(--pink);font-size:6.5px;font-weight:700;line-height:1.3;margin-top:5px}
.course ul{list-style:none}
.course li::before{content:"• "}
.dates{border-collapse:collapse;font-size:6px;color:var(--ink)}
.dates td{padding:0 10px 0 0;line-height:1.35}
.footnote{position:absolute;left:12px;bottom:5px;width:110px;color:var(--white);font-size:5px;line-height:1.3}
</style>
</head>
<body>

<section class="sheet sheet--outside" aria-label="Außenseite">
  <div class="top-strip"></div>

  <div class="photo person-photo" role="img" aria-label="Porträtfoto der Kursleiterin"></div>
  <div class="col col--person">
    <p class="title-red">zur person</p>
    <p>Ehenihit offictem. Pudi ius maio. Omnime volore nullaciae. Et occus, adipsunt ut la voloreprem reria asimeni moditatia excea volo comniscipsum repudandit exerfer namusam ut volectatem. Volut dolesen imagnate sinis electe sumquas es maionectes doloreptate volupidem este voluptas non nus exerum que consed eaquidit et ut eligento experro bero berspernum faces dolum sit maximus perum unti berarum que dolor mos volorer uptaeritat aut vel maximil itatur, et aboriasincto con res ant, volorpo repuditatia ipsuntur, verem ipiet int que erchill oreseriate liciendi tem recearic hillab isquiditin pa corpori dolupta inci tes doles minimin que re cullupt aspidenit quissin aximintest, same nonsequ isciat. Qui alit et, omnim dolut voluptum as e</p>
  </div>

  <div class="col col--payment">
    <p class="title-red">zahlungsbedingungen</p>
    <p>Ehenihit offictem. Pudi ius maio. Omnime volore nullaciae. Et occus, adipsunt ut la voloreprem reria asimeni moditatia excea volo comniscipsum repudandit exerfer namusam ut volectatem. Volut dolesen imagnate sinis electe sumquas es maionectes doloreptate volupidem este voluptas non nus exerum que consed eaquidit et ut eligento experro bero berspernum faces dolum sit maximus perum unti berarum que dolor mos volorer uptaeritat aut vel maximil itatur, et aboriasincto con res ant. Qui alit et, omnim dolut voluptum as e</p>
  </div>
  <div class="photo detail-photo detail-photo--eye" role="img" aria-label="Detailfoto eines geschminkten Auges"></div>
  <div class="photo detail-photo detail-photo--lips" role="img" aria-label="Detailfoto geschminkter Lippen"></div>

  <div class="cover" role="img" aria-label="Titelfoto: Model mit hellem Kurzhaar im dunklen Kleid"></div>
  <h1 class="cover-title">mira makeup academy</h1>

  <svg class="bottom-wave" viewBox="0 0 640 40" preserveAspectRatio="none" aria-hidden="true">
    <path d="M0 18 C150 4 300 38 440 24 C530 15 590 16 640 8 L640 40 L0 40Z" fill="var(--navy)"/>
    <path d="M0 26 C150 12 300 46 440 32 C530 23 590 24 640 16" fill="none" stroke="var(--blue-light)" stroke-width="3"/>
  </svg>

  <div class="brand">
    <div class="brand-name">Mira</div>
    <div class="brand-sub">makeup by mira lenz</div>
  </div>
</section>

<section class="sheet sheet--inside" aria-label="Innenseite">
  <div class="inside-photo" role="img" aria-label="Blass getöntes Porträtfoto eines Models als Hintergrund"></div>
  <div class="top-strip"></div>

  <article class="course course--one">
    <h2>basic education teil 1</h2>
    <p>in diesem workshop wird basiswissen vermittelt, mit dem jeder friseur professionell sein beauty-salonprogramm abrunden und das sortiment seiner dienstleistungen erweitern kann.</p>
    <h3>inhalte auf einen blick:</h3>
    <ul>
      <li>produktwissen</li><li>gesichtsvermessungen</li><li>optimierung der gesichtsformen</li><li>augenmakeups</li><li>makeup für verschiedene augenformen</li><li>augen-makeup für brillenträgerinnen</li><li>tages-makeup</li><li>abend-makeup</li><li>special-makeup (wimpern kleben, auf bringen von glitter und accessoires)</li>
    </ul>
    <h3>termine</h3>
    <table class="dates">
      <tr><td>so</td><td>08.05.2011</td><td>10-18 uhr</td></tr>
      <tr><td>mo</td><td>09.05.2011</td><td>10-14 uhr</td></tr>
      <tr><td>so</td><td>15.05.2011</td><td>10-18 uhr</td></tr>
      <tr><td>mo</td><td>16.05.2011</td><td>10-14 uhr</td></tr>
      <tr><td>so</td><td>22.05.2011</td><td>10-18 uhr</td></tr>
      <tr><td>mo</td><td>23.05.2011</td><td>10-14 uhr</td></tr>
      <tr><td>so</td><td>29.05.2011</td><td>10-18 uhr</td></tr>
      <tr><td>mo</td><td>30.05.2011</td><td>10-14 uhr</td></tr>
    </table>
    <h3>voraussetzungen</h3>
    <p>dieser kurs ist geeignet für einsteiger und für alle, die vorhandenes wissen auffrischen oder vertiefen wollen.</p>
    <h3>kosten</h3>
    <p>€ 990 exkl. mwst.<br>anmeldung<br>bis 01.03.2011<br>mira@lockenwerkstattxy.at oder 01 555 01 23</p>
  </article>

  <article class="course course--two">
    <h2>junior makeup artist teil 2</h2>
    <p>junior makeup artists, die diesen kurs absolviert haben, sind in der lage, makeup- und typberatung, foto- und anti-aging-makeup anzubieten. die inhalte befassen sich noch detaillierter als im ersten teil mit farben und formen beim schminken und die techniken werden von der beratung bis zur umsetzung trainiert.</p>
    <h3>inhalte auf einen blick:</h3>
    <ul>
      <li>haut</li><li>anti-aging-makeup</li><li>foto-makeup</li><li>schwarz/weiß foto-makeup</li><li>männer-makeup</li><li>typberatung</li><li>makeup beratung</li><li>braut-makeup</li>
    </ul>
    <h3>termine</h3>
    <table class="dates">
      <tr><td>so</td><td>10.07.2011</td><td>10-18 uhr</td></tr>
      <tr><td>mo</td><td>11.07.2011</td><td>10-14 uhr</td></tr>
      <tr><td>so</td><td>17.07.2011</td><td>10-18 uhr</td></tr>
      <tr><td>mo</td><td>18.07.2011</td><td>10-14 uhr</td></tr>
      <tr><td>so</td><td>24.07.2011</td><td>10-18 uhr</td></tr>
      <tr><td>mo</td><td>25.07.2011</td><td>10-14 uhr</td></tr>
      <tr><td>so</td><td>31.07.2011</td><td>10-18 uhr</td></tr>
      <tr><td>mo</td><td>01.08.2011</td><td>10-14 uhr</td></tr>
    </table>
    <h3>voraussetzungen</h3>
    <p>dieser kurs ist geeignet für friseure mit basiswissen, talentierte quereinsteiger und teilnehmer des ersten kurses, makeup basics. teilnehmer von makeup basics erhalten nach diesem kurs auch das junior makeup artist diplom.</p>
    <h3>kosten</h3>
    <p>€ 990 exkl. mwst.</p>
    <h3>anmeldung</h3>
    <p>bis 02.05.2011<br>mira@lockenwerkstattxy.at oder 01 555 01 23</p>
  </article>

  <article class="course course--three">
    <h2>senior makeup artist teil 3</h2>
    <p>in der dritten stufe werden kreative techniken und formen vertieft, von shows und editorials bis zu bühne und film. die unbedingt notwendige epochen-kenntnis bildet die basis, um verschiedener epochen zu schminken aber auch abzuwandeln. in diesem workshop nehmen wir uns besonders viel zeit für techniken zu perfektionieren und deiner makeupkunst eine individuelle note zu geben.</p>
    <h3>inhalte auf einen blick:</h3>
    <ul>
      <li>epochen makeup (20er bis 90er jahre)</li><li>verschiedene kulturen/historische makeups (geisha, orientalisches makeup,...)</li><li>geschichte des makeup</li><li>laufsteg makeup (konzepterstellung, makeup-design, planung)</li><li>x-treme makeup/phantasie-makeup</li>
    </ul>
    <h3>termine</h3>
    <table class="dates">
      <tr><td>so</td><td>11.09.2011</td><td>10-18 uhr</td></tr>
      <tr><td>mo</td><td>12.09.2011</td><td>10-14 uhr</td></tr>
      <tr><td>so</td><td>18.09.2011</td><td>10-18 uhr</td></tr>
      <tr><td>mo</td><td>19.09.2011</td><td>10-14 uhr</td></tr>
      <tr><td>so</td><td>25.09.2011</td><td>10-18 uhr</td></tr>
      <tr><td>mo</td><td>26.09.2011</td><td>10-14 uhr</td></tr>
      <tr><td>so</td><td>02.10.2011</td><td>10-18 uhr</td></tr>
      <tr><td>mo</td><td>03.10.2011</td><td>10-14 uhr</td></tr>
    </table>
    <h3>voraussetzungen</h3>
    <p>dieser kurs ist geeignet für kreative künstler mit vorbildung und rundet die ausbildung für teilnehmer von teil 1 und 2 (makeup basics und junior makeup artist) perfekt ab. der kurs endet mit einer schriftlichen und praktischen prüfung. teilnehmer, die auch die ersten beiden kurse besucht haben, erhalten nach bestandener prüfung ein visagistendiplom.</p>
    <h3>kosten</h3>
    <p>€ 990 exkl. mwst.<br>anmeldung bis 01.07.2011<br>mira@lockenwerkstattxy.at oder 01 555 01 23</p>
  </article>

  <svg class="bottom-wave" viewBox="0 0 640 40" preserveAspectRatio="none" aria-hidden="true">
    <path d="M0 8 C160 28 300 34 450 26 C540 21 600 14 640 8 L640 40 L0 40Z" fill="var(--navy)"/>
    <path d="M0 16 C160 36 300 42 450 34 C540 29 600 22 640 16" fill="none" stroke="var(--blue-light)" stroke-width="3"/>
  </svg>
  <p class="footnote">bei anmeldung für alle drei kurse bis 01.03.2011 werden 5% rabatt auf den gesamtpreis gewährt.</p>
</section>

</body>
</html>
```